Melvin Otrasko Consulting Corporation
Independent Insurance and Reinsurance Consultants
Melvin Otrasko Consulting Corporation - Consulting
Creative Brief
Professional
Melvin Otrasko, MBA, CPCU
Insurance and Reinsurance Consultant
3816C Verlune Court Carlsbad, CA 92011
motrasko@motraskoadvise.com
www.motraskoadvise.com

```html
<!DOCTYPE html>
<html lang="en">
<head>
<meta charset="utf-8">
<title>Melvin Otrasko Consulting Corporation – Business Cards</title>
<link href="https://fonts.googleapis.com/css2?family=Cormorant+Garamond:wght@500;600&family=Open+Sans:wght@400;600;700&display=swap" rel="stylesheet">
<style>
  :root {
    --canvas: #eceeef;
    --card-white: #ffffff;
    --brand-blue: #1d5cb4;
    --brand-blue-deep: #124a9c;
    --brand-blue-light: #4a8fe0;
    --text-dark: #2e2e2e;
    --text-mid: #555555;
    --divider: #3a3a3a;
    --emblem-light: rgba(190, 195, 200, 0.28);
    --emblem-blue: rgba(140, 190, 235, 0.25);
  }
  * { margin: 0; padding: 0; box-sizing: border-box; }
  html, body { width: 1200px; height: 794px; overflow: hidden; }
  body {
    background: var(--canvas);
    position: relative;
    font-family: "Open Sans", Arial, sans-serif;
  }
  .card {
    position: absolute;
    border-radius: 20px;
    overflow: hidden;
  }
  .card--front { left: 300px; top: 67px; width: 533px; height: 305px; background: var(--card-white); }
  .card--back-white { left: 24px; top: 432px; width: 533px; height: 300px; background: var(--card-white); }
  .card--back-blue {
    left: 593px; top: 432px; width: 535px; height: 300px;
    background: radial-gradient(ellipse at 50% 45%, var(--brand-blue-light) 0%, var(--brand-blue) 55%, var(--brand-blue-deep) 100%);
  }
  .emblem {
    position: absolute;
    border-radius: 40px;
    background: radial-gradient(ellipse at center, var(--emblem-light) 0%, rgba(255,255,255,0) 72%);
  }
  .card--back-blue .emblem { background: radial-gradient(ellipse at center, var(--emblem-blue) 0%, rgba(255,255,255,0) 72%); }
  .wordmark {
    position: absolute; left: 0; right: 0; text-align: center;
    color: var(--brand-blue);
  }
  .wordmark__name {
    font-family: "Cormorant Garamond", "Times New Roman", serif;
    font-weight: 500;
    font-size: 40px;
    letter-spacing: 1px;
    line-height: 1;
  }
  .wordmark__tag {
    font-family: "Open Sans", Arial, sans-serif;
    font-size: 17px;
    letter-spacing: 3px;
    line-height: 1;
    margin-top: 4px;
  }
  .card--back-blue .wordmark { color: #ffffff; }
  .card--front .wordmark { top: 34px; }
  .card--back-white .wordmark, .card--back-blue .wordmark { top: 116px; }
  .card--back-white .wordmark__name, .card--back-blue .wordmark__name { font-size: 42px; }
  .side-tab {
    position: absolute; left: 0; top: 149px; width: 29px; height: 79px;
    background: linear-gradient(180deg, var(--brand-blue-light), var(--brand-blue-deep));
  }
  .person { position: absolute; left: 48px; top: 164px; }
  .person__name { font-weight: 700; font-size: 17px; color: var(--brand-blue); line-height: 22px; }
  .person__role { font-size: 13px; color: var(--text-mid); margin-top: 2px; }
  .divider { position: absolute; left: 300px; top: 118px; width: 1.5px; height: 175px; background: var(--divider); }
  .contact { position: absolute; left: 316px; top: 118px; font-size: 13px; color: var(--text-dark); }
  .contact__address { line-height: 19px; margin-bottom: 8px; }
  .contact__row { display: flex; align-items: center; height: 19px; }
  .contact__row svg { width: 13px; height: 13px; margin-right: 7px; flex: none; }
  .web-line {
    position: absolute; left: 0; right: 0; top: 268px; text-align: center;
    font-size: 14px; color: var(--text-dark); letter-spacing: 0.3px;
  }
  .web-line strong { font-weight: 700; }
  .card--back-blue .web-line { color: #ffffff; }
</style>
</head>
<body>

  <section class="card card--front">
    <div class="emblem" role="img" aria-label="Faint scales of justice emblem" style="left:96px; top:135px; width:160px; height:160px;"></div>
    <div class="wordmark">
      <div class="wordmark__name">MELVIN OTRASKO</div>
      <div class="wordmark__tag">CONSULTING CORPORATION</div>
    </div>
    <div class="side-tab"></div>
    <div class="person">
      <div class="person__name">Melvin Otrasko, MBA, CPCU</div>
      <div class="person__role">Insurance and Reinsurance Consultant</div>
    </div>
    <div class="divider"></div>
    <div class="contact">
      <div class="contact__address">3816C Verlune Court<br>Carlsbad, CA 92011</div>
      <div class="contact__row">
        <svg viewBox="0 0 16 16"><path d="M4 1.5l2.2 3-1.3 1.6c.9 2 2.5 3.6 4.5 4.5l1.6-1.3 3 2.2-1.2 2.5C7.5 14 2 8.5 1.5 3z" fill="#2e2e2e"/></svg>
        <span>6194418207</span>
      </div>
      <div class="contact__row">
        <svg viewBox="0 0 16 16"><rect x="4" y="1" width="8" height="14" rx="1.5" fill="#2e2e2e"/><rect x="5.5" y="3" width="5" height="8" fill="#fff"/><circle cx="8" cy="13" r=".9" fill="#fff"/></svg>
        <span>6194418207</span>
      </div>
      <div class="contact__row">
        <svg viewBox="0 0 16 16"><rect x="4" y="1" width="8" height="5" fill="#2e2e2e"/><rect x="1" y="6" width="14" height="7" rx="1" fill="#2e2e2e"/><rect x="4" y="10" width="8" height="5" fill="#fff" stroke="#2e2e2e"/></svg>
        <span>7603392846</span>
      </div>
      <div class="contact__row">
        <svg viewBox="0 0 16 16"><circle cx="8" cy="8" r="7" fill="#2e2e2e"/><text x="8" y="11.5" font-size="10" text-anchor="middle" fill="#fff" font-family="Arial, sans-serif" font-weight="700">@</text></svg>
        <span>motrasko@motraskoadvise.com</span>
      </div>
      <div class="contact__row">
        <svg viewBox="0 0 16 16"><circle cx="8" cy="8" r="7" fill="#2e2e2e"/><path d="M1 8h14M8 1c-3 3-3 11 0 14M8 1c3 3 3 11 0 14" stroke="#fff" stroke-width="1" fill="none"/></svg>
        <span>www.motraskoadvise.com</span>
      </div>
    </div>
  </section>

  <section class="card card--back-white">
    <div class="emblem" role="img" aria-label="Faint scales of justice emblem" style="left:180px; top:10px; width:170px; height:285px;"></div>
    <div class="wordmark">
      <div class="wordmark__name">MELVIN OTRASKO</div>
      <div class="wordmark__tag">CONSULTING CORPORATION</div>
    </div>
    <div class="web-line">www.<strong>motraskoadvise</strong>.com</div>
  </section>

  <section class="card card--back-blue">
    <div class="emblem" role="img" aria-label="Faint scales of justice emblem" style="left:185px; top:10px; width:170px; height:285px;"></div>
    <div class="wordmark">
      <div class="wordmark__name">MELVIN OTRASKO</div>
      <div class="wordmark__tag">CONSULTING CORPORATION</div>
    </div>
    <div class="web-line">www.<strong>motraskoadvise</strong>.com</div>
  </section>

</body>
</html>
```